Flyer-Design für Ernährungsexpertin
Zielgruppe
Ich bin Ernährungsexpertin. Meine Zielgruppe sind Menschen, denen es nicht gut geht und die bereit sind ihre Gesundheit selbst in die Hand zu nehmen.
Aufgabenstellung
Farblich in Anlehnung an meine Homepage www.lebensfrischwerk.de. grün: #99cc33, grau: #f4f1ef
Das Design soll man mit Gesundheit und Wohlfühlen assoziieren.
Textmäßig sollen drei Aspekte aufgegriffen werden (sinngemäß):
- Ich helfe Ihnen gesund und nachhaltig Ihr Wohlfühlgewicht zu erreichen.
- Vielen Beschwerden liegt eine ungünstige Ernährung zugrunde. Ich suche nach der Ursache und setze hier an.
- Prävention statt Behandlung: in meinem Präventionskurs 'Gewichtsmanagement' entwickeln Sie einen neuen Lifestyle, der sich gut anfühlt.
Kontaktdaten:
www.lebensfrischwerk.de
Merle@lebensfrischwerk.de

```html
<!DOCTYPE html>
<html lang="de">
<head>
<meta charset="utf-8">
<title>Lebensfrischwerk – Flyer</title>
<link href="https://fonts.googleapis.com/css2?family=EB+Garamond:wght@400;500&family=Roboto:wght@300;400;500&display=swap" rel="stylesheet">
<style>
  :root {
    --green: #5cad2f;
    --green-light: #8fc33c;
    --ink: #1a1a1a;
    --paper: #ffffff;
    --backdrop: #e9e9e9;
    --serif: "EB Garamond", Georgia, serif;
    --sans: "Roboto", Arial, sans-serif;
  }
  * { box-sizing: border-box; margin: 0; padding: 0; }
  html, body { width: 717px; height: 1200px; overflow: hidden; }
  body { background: var(--backdrop); position: relative; font-family: var(--sans); color: var(--ink); }

  .page {
    position: absolute; top: 270px; width: 310px; height: 660px;
    background: var(--paper); overflow: hidden;
    box-shadow: 0 3px 10px rgba(0,0,0,0.18);
  }
  .page--front { left: 36px; }
  .page--back { left: 371px; }
  .abs { position: absolute; }

  /* Front */
  .brand { left: 0; right: 0; top: 46px; text-align: center; }
  .brand__name { font-family: var(--serif); font-size: 25px; color: var(--ink); }
  .brand__tagline { font-size: 7px; color: var(--green); margin-top: 2px; }
  .headline { left: 29px; top: 112px; font-family: var(--serif); font-size: 30px; line-height: 32px; font-weight: 400; }
  .lead { left: 29px; top: 188px; width: 260px; font-size: 12.2px; line-height: 16.5px; color: var(--green); }
  .photo-hero {
    left: 0; top: 250px; width: 310px; height: 340px;
    background: linear-gradient(180deg, #f2f2f0 0%, #dfe3dc 30%, #7f9a70 58%, #4f74a8 80%, #3d64a0 100%);
  }
  .front-wave { left: 0; top: 540px; }
  .visit { left: 25px; top: 606px; color: #fff; font-size: 12px; font-weight: 300; line-height: 17px; }
  .visit__url { font-size: 14px; font-weight: 400; }

  /* Back */
  .back-top { left: 0; top: 0; }
  .promise { left: 20px; right: 20px; top: 43px; text-align: center; color: #fff; font-size: 16.5px; line-height: 21.5px; font-weight: 400; }
  .badge {
    left: 188px; top: 113px; width: 104px; height: 104px; border-radius: 50%;
    background: var(--green-light); border: 2px solid #fff; box-shadow: 0 0 0 1px var(--green-light);
    color: #fff; text-align: center; display: flex; flex-direction: column; justify-content: center;
    font-size: 12.5px; line-height: 17px; transform: rotate(4deg);
  }
  .badge strong { font-weight: 500; }
  .cta { left: 29px; top: 215px; font-family: var(--serif); font-size: 30px; line-height: 32px; font-weight: 400; }
  .cta-url { left: 29px; top: 283px; font-size: 15px; font-weight: 500; color: var(--green); }
  .photo-food {
    left: 17px; top: 345px; width: 276px; height: 88px; border-radius: 40px 40px 6px 6px;
    background: linear-gradient(90deg, #6a9a3a 0%, #d8492e 20%, #f0a23a 40%, #9cbf4a 55%, #e6c44a 70%, #5b8f34 85%, #c43b2c 100%);
  }
  .course { left: 27px; top: 459px; width: 258px; height: 88px; border: 1.5px solid var(--green);
    display: flex; align-items: center; justify-content: center; text-align: center;
    font-size: 12px; line-height: 17.5px; padding: 0 6px; }
  .course__lead { color: var(--green); font-weight: 500; }
  .portrait { left: 27px; top: 569px; width: 58px; height: 58px; border-radius: 50%;
    background: radial-gradient(circle at 50% 45%, #6b5a4e 0%, #3f4a33 45%, #5f8a40 100%); }
  .contact { left: 96px; top: 573px; }
  .contact__name { font-family: var(--serif); font-size: 13px; font-weight: 500; }
  .contact__role { font-size: 8.3px; color: #444; margin-top: 1px; }
  .contact__line { font-size: 8.5px; margin-top: 4px; display: flex; align-items: center; gap: 6px; }
  .contact__line svg { width: 9px; height: 9px; }
  .back-footer { left: 0; bottom: 0; width: 310px; height: 15px; background: var(--green); }
</style>
</head>
<body>
  <section class="page page--front">
    <div class="abs brand">
      <div class="brand__name">Lebensfrischwerk</div>
      <div class="brand__tagline">Dein Wohlbefinden beginnt auf deinem Teller</div>
    </div>
    <h1 class="abs headline">Zeit, dass Leben<br>richtig zu genießen!</h1>
    <p class="abs lead">Vielen Beschwerden liegt eine ungünstige Ernährung zugrunde. Ich suche nach der Ursache und setze hier an.</p>
    <div class="abs photo-hero" role="img" aria-label="Foto: lächelnde Frau mit Strohhut und Jeansjacke breitet die Arme in der Natur aus"></div>
    <svg class="abs front-wave" width="310" height="120" viewBox="0 0 310 120">
      <path d="M0 42 C 90 20, 180 50, 310 62 L310 120 L0 120 Z" fill="#5cad2f"/>
      <path d="M0 36 C 90 14, 180 44, 310 56" fill="none" stroke="#5cad2f" stroke-width="1.3"/>
    </svg>
    <div class="abs visit">Besuchen Sie mich auf<br><span class="visit__url">www.lebensfrischwerk.de</span></div>
  </section>

  <section class="page page--back">
    <svg class="abs back-top" width="310" height="190" viewBox="0 0 310 190">
      <path d="M0 0 H310 V176 C 240 170, 200 148, 100 140 C 60 138, 25 144, 0 150 Z" fill="#5cad2f"/>
      <path d="M0 157 C 25 151, 60 145, 100 147 C 200 155, 240 177, 310 183" fill="none" stroke="#5cad2f" stroke-width="1.3"/>
    </svg>
    <p class="abs promise">Ich helfe Ihnen gesund und nachhaltig Ihr Wohlfühlgewicht zu erreichen.</p>
    <div class="abs badge"><span>Erleben</span><span>Sie <strong>ein neues</strong></span><strong>Körpergefühl.</strong></div>
    <h2 class="abs cta">Lassen Sie<br>sich online beraten!</h2>
    <div class="abs cta-url">www.lebensfrischwerk.de</div>
    <div class="abs photo-food" role="img" aria-label="Foto: Auswahl an frischem Obst, Gemüse, Fisch und Käse"></div>
    <div class="abs course"><p><span class="course__lead">Prävention statt Behandlung:</span> in meinem Präventionskurs 'Gewichtsmanagement' entwickeln Sie einen neuen Lifestyle, der sich gut anfühlt.</p></div>
    <div class="abs portrait" role="img" aria-label="Porträtfoto der Ernährungsexpertin im Grünen"></div>
    <div class="abs contact">
      <div class="contact__name">Merle Brandauer</div>
      <div class="contact__role">Ernährungsexpertin &amp; Personal Trainerin</div>
      <div class="contact__line">
        <svg viewBox="0 0 24 24"><path d="M6 3l3 0 2 5-2 2c1 2 3 4 5 5l2-2 5 2v3c0 1-1 2-2 2C10 20 4 14 4 5c0-1 1-2 2-2z" fill="none" stroke="#5cad2f" stroke-width="2"/></svg>
        0157-38492610
      </div>
      <div class="contact__line">
        <svg viewBox="0 0 24 24"><rect x="3" y="6" width="18" height="13" fill="none" stroke="#5cad2f" stroke-width="2"/><path d="M3 7l9 7 9-7" fill="none" stroke="#5cad2f" stroke-width="2"/></svg>
        merle@lebensfrischwerk.de
      </div>
    </div>
    <div class="abs back-footer"></div>
  </section>
</body>
</html>
```